Brand New Africa Focused Specialty Insurance business needs a slick website

Meridane Underwriting Partners needs a slick website design to launch our business with. we have 3 lines of business to begin with - Political Risk and Trade Credit and Property. (this will extend to 9: Political violence and Terrorism, Construction, Liability, Energy, Aviation, Marine, Parametric and Crisis Management at a later date). We are based in London but are Africa focused and our mission statement Meridane Underwriting Partners provides comprehensive, bespoke insurance risk mitigating solutions to local and global customers, giving them the confidence to grow their businesses sustainably. our tagline is "protecting Africa". Our colours are purple (Red 36, Green 11, Blue 96) and gold (Red 143, Green 137, Blue 53).

Target Market(s)

Brokers
Businesses across africa

Coding

Number of Pages Required

4 page

Font styles to use
Sans Serif
Other font styles liked:
• Cairo (but open to others too)

Requirements
Must have
• Pages:
1. Home page/about us (to include Lines of Business)
2. a page for Property line (we will need to add a link so that people can send an email to the mailbox)
3. a page for Political Risk and Trade Credit ( we will need to add a link so that people can send an email to the mailbox)
3. a page about our people (photos not yet taken for this)
4. a careers page
we have a lot of text for the above, we just need to fine tune it

must be tied to the colour scheme I detailed above.

the font for the logo is called Cairo
Nice to have
• https://www.torvalex-mutual.com/ - we like the look of this website, but perhaps less colour
Should not have
• Any African animal like Lions or Zebras

```html
<!DOCTYPE html>
<html lang="en">
<head>
<meta charset="utf-8">
<title>Meridane Underwriting Partners – Protecting Africa</title>
<link href="https://fonts.googleapis.com/css2?family=Arimo:ital,wght@0,400;0,700;1,400;1,700&family=Saira+Semi+Condensed:wght@700;800&display=swap" rel="stylesheet">
<style>
:root{
  --purple:#240b60;
  --gold:#8f8935;
  --ink:#333333;
  --muted:#555555;
  --band:#ececec;
  --footer:#262626;
  --footer-edge:#3a3a3a;
  --white:#ffffff;
}
*{box-sizing:border-box;margin:0;padding:0}
html,body{width:1200px;height:4142px;overflow:hidden}
body{position:relative;background:var(--white);font-family:"Arimo",Arial,sans-serif;color:var(--ink)}
.abs{position:absolute}
.display{font-family:"Saira Semi Condensed","Arial Narrow",sans-serif;font-weight:800;letter-spacing:.5px}

/* header */
.site-header{position:absolute;left:0;top:0;width:1200px;height:80px;background:var(--white);z-index:2}
.brand{position:absolute;left:148px;top:6px;display:flex;align-items:center;gap:12px}
.brand-mark{width:68px;height:68px;border-radius:50%;border:3px solid var(--gold)}
.brand-name{font-weight:700;font-size:16px;color:var(--purple);line-height:1.2;white-space:nowrap}
.main-nav a{position:absolute;top:27px;font-size:19px;color:#333;text-decoration:none}

/* hero */
.hero-title{left:0;width:1200px;top:266px;text-align:center;font-size:54px;line-height:66px;color:var(--white)}
.hero-text{left:140px;width:920px;top:355px;text-align:center;font-size:23px;line-height:44px;color:var(--white)}
.btn{display:block;background:var(--gold);color:var(--white);text-align:center;border-radius:6px;text-decoration:none}
.hero-btn{left:512px;top:468px;width:177px;height:55px;line-height:55px;font-weight:700;font-size:20px}
.dot{position:absolute;border-radius:50%}

/* about */
.section-title{color:var(--purple);font-size:35px;line-height:44px}
.about-title{left:114px;top:898px}
.body-copy{font-size:15.5px;line-height:33.5px;color:var(--ink)}
.about-copy{left:114px;top:966px;width:590px}
.about-btn{left:111px;top:1258px;width:132px;height:50px;line-height:50px;font-size:16px}

/* lines of business */
.lob-band{left:0;top:1405px;width:1200px;height:577px;background:linear-gradient(120deg,#3a1c70 0%,#5a3590 45%,#3b1b6e 100%)}
.lob-title{left:0;width:1200px;top:1450px;text-align:center;color:var(--white);font-size:35px;line-height:44px}
.lob-intro{left:170px;width:860px;top:1525px;text-align:center;color:var(--white);font-size:16px;line-height:26px}
.lob-card{position:absolute;top:1612px;width:302px;height:307px;background:var(--white);text-align:center}
.lob-card .thumb{position:absolute;left:5px;top:5px;width:292px;height:174px;border-radius:4px}
.lob-card h3{position:absolute;left:0;width:100%;top:205px;font-size:20px;line-height:26px;color:#222}
.lob-card p{position:absolute;left:18px;right:18px;top:237px;font-size:16.5px;line-height:26px;color:#222}

/* comprehensive */
.risk-frame{left:111px;top:2093px;width:367px;height:320px;background:var(--gold);border-radius:6px}
.risk-photo{left:105px;top:2108px;width:362px;height:370px;border-radius:4px;border:3px solid var(--white)}
.risk-title{left:528px;top:2088px;font-size:31px}
.risk-copy{left:528px;top:2156px;width:570px}
.risk-btn{left:528px;top:2430px;width:132px;height:50px;line-height:50px;font-size:16px}

/* blog */
.blog-band{left:0;top:2589px;width:1190px;height:610px;background:var(--band)}
.blog-title{left:0;width:1200px;top:2633px;text-align:center;font-size:35px}
.post{position:absolute;top:2740px;width:314px;height:336px;background:var(--white);text-align:center;box-shadow:0 1px 3px rgba(0,0,0,.08)}
.post .thumb{position:absolute;left:3px;top:0;width:308px;height:175px}
.post h4{position:absolute;left:0;width:100%;top:198px;font-size:17.5px;color:#222}
.post .date{position:absolute;left:0;width:100%;top:232px;font-size:15.5px;color:#333;display:flex;justify-content:center;align-items:center;gap:10px}
.post p{position:absolute;left:20px;right:20px;top:268px;font-size:16.5px;line-height:27px;color:var(--muted)}

/* testimonials */
.say-title{left:0;width:1200px;top:3273px;text-align:center;font-size:37px;line-height:46px;color:#222}
.avatar{left:566px;top:3359px;width:94px;height:94px;border-radius:50%;background:radial-gradient(circle at 50% 40%,#c9b6a3,#6f6258);border:3px solid #ddd}
.quote-text{left:240px;width:720px;top:3463px;text-align:center;font-size:15px;line-height:30.5px;color:var(--muted)}
.quote-author{left:0;width:1200px;top:3576px;text-align:center;font-size:14.5px;font-style:italic;font-weight:700;color:#444}
.quote-mark{font-family:"Saira Semi Condensed","Arial Narrow",sans-serif;font-weight:800;color:#8a8a8a;font-size:120px;line-height:1}
.arrow-btn{width:46px;height:46px;border-radius:50%}

/* footer */
.foot-head{color:var(--white);font-size:29px;font-weight:700}
.foot-text{color:var(--white);font-size:18.5px;line-height:34px}
.foot-icon{width:42px;height:42px;border-radius:50%;background:var(--gold)}
.social{width:38px;height:38px;border-radius:50%;border:2px solid #cfcfcf}
.copyright{left:0;width:1200px;top:4088px;text-align:center;color:var(--white);font-size:13px}
</style>
</head>
<body>

<header class="site-header">
  <div class="brand">
    <span class="brand-mark"></span>
    <span class="brand-name">Meridane Underwriting Partners</span>
  </div>
  <nav class="main-nav">
    <a href="#" style="left:587px">Home</a>
    <a href="#" style="left:676px">About Us</a>
    <a href="#" style="left:796px">Services</a>
    <a href="#" style="left:911px">Bog</a>
    <a href="#" style="left:983px">Contact Us</a>
  </nav>
</header>

<!-- hero -->
<svg class="abs" style="left:0;top:0" width="1200" height="820" role="img" aria-label="Photo of a hand pulling a block labelled risk from a wooden stacking tower">
  <defs>
    <linearGradient id="heroWood" x1="0" y1="0" x2="1" y2="1">
      <stop offset="0" stop-color="#7a5436"/>
      <stop offset=".35" stop-color="#a27a52"/>
      <stop offset=".7" stop-color="#5a3b25"/>
      <stop offset="1" stop-color="#2c211b"/>
    </linearGradient>
  </defs>
  <path d="M0 80 H1200 V690 L160 810 Q80 818 52 745 L0 600 Z" fill="url(#heroWood)"/>
  <path d="M0 80 H1200 V690 L160 810 Q80 818 52 745 L0 600 Z" fill="rgba(0,0,0,.18)"/>
</svg>
<h1 class="abs display hero-title">PROTECTING AFRICA</h1>
<p class="abs hero-text">Lorem ipsum dolor sit amet, consectetur adipiscing elit, sed do eiusmod tempor dolor sit amet, consectetur.Neque porro quisquam est qui dolorem ipsum.</p>
<a class="abs btn hero-btn" href="#">GET STARTED</a>
<span class="dot" style="left:559px;top:708px;width:11px;height:11px;background:#fff"></span>
<span class="dot" style="left:594px;top:708px;width:11px;height:11px;background:#fff"></span>
<span class="dot" style="left:628px;top:708px;width:11px;height:11px;background:rgba(255,255,255,.3)"></span>

<!-- about -->
<h2 class="abs display section-title about-title">ABOUT US</h2>
<p class="abs body-copy about-copy">Sed ut perspiciatis unde omnis iste natus error sit voluptatem accusantium doloremque laudantium, totam rem aperiam, eaque ipsa quae ab illo inventore veritatis et quasi architecto beatae vitae dicta sunt explicabo. Nemo enim ipsam voluptatem quia voluptas sit aspernatur aut odit aut fugit, sed quia consequuntur magni dolores eos qui ratione voluptatem sequi nesciunt. Neque porro quisquam est, qui dolorem ipsum quia dolor sit amet, consectetur, adipisci velit, sed quia non numquam eius modi tempora incidunt ut labore et dolore magnam aliquam quaerat voluptatem. Ut enim ad minima veniam.</p>
<a class="abs btn about-btn" href="#">READ MORE</a>
<svg class="abs" style="left:715px;top:898px" width="370" height="385" role="img" aria-label="Round photo of a hand removing a block from a wooden tower">
  <defs>
    <linearGradient id="aboutPhoto" x1="0" y1="0" x2="1" y2="1">
      <stop offset="0" stop-color="#1c2430"/>
      <stop offset=".55" stop-color="#2e3540"/>
      <stop offset=".6" stop-color="#c9a877"/>
      <stop offset="1" stop-color="#a98556"/>
    </linearGradient>
  </defs>
  <circle cx="182" cy="195" r="180" fill="var(--gold)"/>
  <circle cx="186" cy="180" r="178" fill="url(#aboutPhoto)"/>
</svg>

<!-- lines of business -->
<div class="abs lob-band" role="img" aria-label="Purple tinted photo of a wooden block tower"></div>
<h2 class="abs display lob-title">3 LINES OF BUSINES</h2>
<p class="abs lob-intro">Sed ut perspiciatis unde omnis iste natus error sit voluptatem accusantium doloremque laudantium, totam rem aperiam, eaque ipsa quae ab illo inventore veritatis et quasi architecto beatae vitae dicta sunt explicabo.</p>

<article class="lob-card" style="left:111px">
  <div class="thumb" role="img" aria-label="Silhouettes crossing a gap at sunset" style="background:linear-gradient(180deg,#c46a2a,#f2b548 60%,#5a2a16)"></div>
  <h3 class="display">POLITICAL RISK</h3>
  <p>Neque porro quisquam est qui dolorem ipsum quia dolor sit amet.</p>
</article>
<article class="lob-card" style="left:449px">
  <div class="thumb" role="img" aria-label="Hands holding a payment card and a phone" style="background:linear-gradient(135deg,#6d7a5a,#b7b29a 50%,#3f4a3c)"></div>
  <h3 class="display">TRADE CREDIT</h3>
  <p>Neque porro quisquam est qui dolorem ipsum quia dolor sit amet.</p>
</article>
<article class="lob-card" style="left:785px">
  <div class="thumb" role="img" aria-label="Small wooden house beside stacks of coins" style="background:linear-gradient(135deg,#3e4656,#9aa0ab 55%,#c69b63)"></div>
  <h3 class="display">PROPERTY</h3>
  <p>Neque porro quisquam est qui dolorem ipsum quia dolor sit amet.</p>
</article>
<span class="dot" style="left:1108px;top:1710px;width:7px;height:7px;background:#fff"></span>
<span class="dot" style="left:1108px;top:1730px;width:7px;height:7px;background:#fff"></span>
<span class="dot" style="left:1108px;top:1750px;width:7px;height:7px;background:#fff"></span>

<!-- comprehensive -->
<svg class="abs" style="left:700px;top:2380px" width="500" height="209" aria-hidden="true">
  <polygon points="340,0 500,200 500,209 160,209" fill="#eef0f6"/>
</svg>
<div class="abs risk-frame"></div>
<div class="abs risk-photo" role="img" aria-label="Hand stopping falling wooden dominoes" style="background:linear-gradient(135deg,#3b6c7d,#d9c6a5 55%,#7a5a3b)"></div>
<h2 class="abs display section-title risk-title">RISKS PROVIDES COMPREHENSIV</h2>
<p class="abs body-copy risk-copy">Sed ut perspiciatis unde omnis iste natus error sit voluptatem accusantium doloremque laudantium, totam rem aperiam, eaque ipsa quae ab illo inventore veritatis et quasi architecto beatae vitae dicta sunt explicabo. Nemo enim ipsam voluptatem quia voluptas sit aspernatur aut odit aut fugit, sed quia consequuntur magni dolores eos qui ratione voluptatem sequi nesciunt. Neque porro quisquam est, qui dolorem ipsum quia dolor sit amet, consectetur, adipisci velit, sed quia non numquam eius modi .</p>
<a class="abs btn risk-btn" href="#">READ MORE</a>

<!-- blog -->
<div class="abs blog-band"></div>
<h2 class="abs display section-title blog-title">OUR BLOG</h2>

<article class="post" style="left:108px">
  <div class="thumb" role="img" aria-label="Network of people icons over a business hand" style="background:linear-gradient(135deg,#0f5a6a,#3fa3b0 50%,#0c3a4a)"></div>
  <h4>Neque porro quisquam est</h4>
  <div class="date"><svg width="14" height="14" viewBox="0 0 14 14"><rect x="1" y="2" width="12" height="11" fill="var(--purple)"/><rect x="3" y="6" width="8" height="1.5" fill="#fff"/><rect x="3" y="9" width="8" height="1.5" fill="#fff"/></svg>Sep,4,2020</div>
  <p>Lorem ipsum dolor sit amet, consectetur adipiscing elit, sed do</p>
</article>
<article class="post" style="left:446px">
  <div class="thumb" role="img" aria-label="Hand holding a house key" style="background:linear-gradient(135deg,#2b2b2e,#6b6e75 55%,#1c1c1f)"></div>
  <h4>Neque porro quisquam est</h4>
  <div class="date"><svg width="14" height="14" viewBox="0 0 14 14"><rect x="1" y="2" width="12" height="11" fill="var(--purple)"/><rect x="3" y="6" width="8" height="1.5" fill="#fff"/><rect x="3" y="9" width="8" height="1.5" fill="#fff"/></svg>Sep,4,2020</div>
  <p>Lorem ipsum dolor sit amet, consectetur adipiscing elit, sed do</p>
</article>
<article class="post" style="left:777px">
  <div class="thumb" role="img" aria-label="Street crowd in front of a domed building" style="background:linear-gradient(180deg,#4e78b8,#a9b9cf 45%,#6a4a3c)"></div>
  <h4>Neque porro quisquam est</h4>
  <div class="date"><svg width="14" height="14" viewBox="0 0 14 14"><rect x="1" y="2" width="12" height="11" fill="var(--purple)"/><rect x="3" y="6" width="8" height="1.5" fill="#fff"/><rect x="3" y="9" width="8" height="1.5" fill="#fff"/></svg>Sep,4,2020</div>
  <p>Lorem ipsum dolor sit amet, consectetur adipiscing elit, sed do</p>
</article>
<span class="dot" style="left:578px;top:3124px;width:8px;height:8px;background:#e8a13a"></span>
<span class="dot" style="left:596px;top:3124px;width:8px;height:8px;background:var(--purple)"></span>
<span class="dot" style="left:614px;top:3124px;width:8px;height:8px;background:var(--purple)"></span>

<!-- testimonials -->
<h2 class="abs display say-title">WHAT OUR CUSTOMERS SAY</h2>
<div class="abs avatar" role="img" aria-label="Customer portrait"></div>
<div class="abs quote-mark" style="left:186px;top:3382px">&ldquo;</div>
<div class="abs quote-mark" style="left:944px;top:3496px">&rdquo;</div>
<p class="abs quote-text">Low performer conversations have the potential to become difficult, but the Steady Talk method keeps these conversations factual, blame-free and unemotional, while encouraging low performers to take responsibility for their performance.</p>
<p class="abs quote-author">By Author Name</p>
<svg class="abs arrow-btn" style="left:109px;top:3436px" viewBox="0 0 46 46" aria-label="Previous"><circle cx="23" cy="23" r="23" fill="var(--gold)"/><path d="M29 23H16M21 17l-6 6 6 6" stroke="#fff" stroke-width="3" fill="none"/></svg>
<svg class="abs arrow-btn" style="left:1021px;top:3436px" viewBox="0 0 46 46" aria-label="Next"><circle cx="23" cy="23" r="23" fill="var(--gold)"/><path d="M17 23h13M25 17l6 6-6 6" stroke="#fff" stroke-width="3" fill="none"/></svg>

<!-- footer -->
<svg class="abs" style="left:0;top:3630px" width="1200" height="512" aria-hidden="true">
  <path d="M1120 20 L1200 200 V512 H1000 Z" fill="var(--footer-edge)"/>
  <path d="M0 135 L1050 15 Q1110 8 1135 65 L1200 215 V512 H0 Z" fill="var(--footer)"/>
</svg>

<h3 class="abs foot-head" style="left:108px;top:3795px">CONTACT US</h3>
<span class="abs foot-icon" style="left:104px;top:3862px"></span>
<svg class="abs" style="left:115px;top:3871px" width="20" height="24" viewBox="0 0 20 24"><path d="M10 1C5 1 2 5 2 9c0 6 8 14 8 14s8-8 8-14c0-4-3-8-8-8z" fill="#fff"/><circle cx="10" cy="9" r="3" fill="var(--gold)"/></svg>
<p class="abs foot-text" style="left:176px;top:3855px">PO Box 4470<br>Harwell Yard, London</p>
<span class="abs foot-icon" style="left:104px;top:3940px"></span>
<svg class="abs" style="left:115px;top:3951px" width="20" height="20" viewBox="0 0 20 20"><path d="M4 1l4 4-2 3c1 3 3 5 6 6l3-2 4 4-3 3C8 19 1 12 1 4z" fill="#fff"/></svg>
<p class="abs foot-text" style="left:176px;top:3944px">Tel: (361)555-0142</p>
<span class="abs foot-icon" style="left:104px;top:4002px"></span>
<svg class="abs" style="left:114px;top:4015px" width="22" height="16" viewBox="0 0 22 16"><rect x="1" y="1" width="20" height="14" fill="#fff"/><path d="M1 1l10 8 10-8" stroke="var(--gold)" stroke-width="2" fill="none"/></svg>
<p class="abs foot-text" style="left:176px;top:4007px">Email:info@meridane.com</p>

<div class="abs" style="left:492px;top:3786px;display:flex;align-items:center;gap:10px">
  <span style="width:74px;height:74px;border-radius:50%;border:3px solid #fff;display:block"></span>
  <span style="color:#fff;font-weight:700;font-size:16px;line-height:1.2;width:190px">Meridane Underwriting Partners</span>
</div>
<p class="abs foot-text" style="left:430px;width:340px;top:3877px;text-align:center;font-size:17.5px;line-height:30px">Neque porro quisquam est qui dolorem ipsum quia dolor sit amet.</p>

<p class="abs foot-text" style="left:845px;top:3795px;font-size:19px">CONNECT ON SOCIAL MEDIA</p>
<span class="abs social" style="left:884px;top:3854px"></span>
<span class="abs social" style="left:937px;top:3854px"></span>
<span class="abs social" style="left:993px;top:3854px"></span>

<p class="abs copyright">Copyrights &copy; 2020 Copyrights Company Name | All Rights Reserved</p>

</body>
</html>
```